Willow Ascent Services Business Card Design

I require a business card design for my business Willow Ascent Services. The purpose of this business is to enable people to make positive change in their lives. This business offers life coaching, hypnotherapy and facilitation services. The slogan is 'Rise from the ashes and live the life you want.' Coaching services will be available internationally whilst the hypnotherapy and facilitation services will focus on delivery in south east Queensland.

The business card should be crisp, clean, professional and give the client positive feelings of achieving success.

The logo must be representative of a Willow Ascent from the ashes which is a symbol of regeneration and new life. My preference is a black Phoenix on a white background similar to the Phoenix image attached to this brief. I'm happy to see other concepts you have too. The logo and business name must be scalable so it can be printed on a large outdoor sign. Therefore the following files must be provided as a minimum:
-Business card
-Logo on it's own
-Business name on it's own

The following detail must appear on either the front/back of the business card
-Logo
-Willow Ascent Services
-Rise from the ashes and live the life you want.
-Personal and business success through
-Coaching | Hypnotherapy | Facilitation
-Greta Halloway
-Founder

-Life Coach
-Clinical Hypnotherapist
-MBA (Project Management specialisation)
-Neuro Linguistic Programming Practitioner

-0412 835 076
-E: willowascent.au@kestrelmail.com
-www.willow-ascent.com.au
-Contact us now for your free 20min assessment

Please feel free to ask me as many questions as you like :) Thank you.

Hi all,  friendly reminder that the logo needs to be your own design and cannot be a Framequarry or other purchased or free image.  

Thanks heaps
Keep the great designs coming in. You're all so talented.
Greta

• Feedback from older people is that black backgrounds with lighter fonts are difficult to read so please no black backgrounds.

```html
<!DOCTYPE html>
<html lang="en">
<head>
<meta charset="utf-8">
<title>Willow Ascent Services – Business Card</title>
<link rel="stylesheet" href="https://fonts.googleapis.com/css2?family=Open+Sans:wght@300;400;600;700&display=swap">
<style>
  :root {
    --backdrop: #e8e8e6;
    --card-light: #f7f7f6;
    --card-edge: #dcdcda;
    --ink-dark: #1e1e1e;
    --ink-body: #3c3c3c;
    --brand-blue: #1a8fd6;
    --mark-grey: #3a3a3a;
  }
  * { margin: 0; padding: 0; box-sizing: border-box; }
  html, body {
    width: 1200px; height: 1200px; overflow: hidden;
    background: var(--backdrop);
    font-family: "Open Sans", Arial, sans-serif;
  }
  .canvas { position: relative; width: 1200px; height: 1200px; }

  .card {
    position: absolute; width: 553px; height: 346px; overflow: hidden;
    background: var(--card-light); color: var(--ink-dark);
    border: 1px solid var(--card-edge);
  }
  .card--back { left: 324px; top: 202px; }
  .card--front { left: 323px; top: 672px; }

  .card-decoration { position: absolute; }
  .card--back .card-decoration {
    left: 345px; top: 0; width: 208px; height: 280px;
    background: radial-gradient(ellipse at 55% 45%, rgba(0,0,0,0.06), rgba(0,0,0,0) 70%);
  }
  .card--front .card-decoration {
    left: 420px; top: 0; width: 133px; height: 170px;
    background: radial-gradient(ellipse at 60% 40%, rgba(0,0,0,0.07), rgba(0,0,0,0) 70%);
  }

  .services-title {
    position: absolute; left: 34px; top: 72px;
    font-size: 15px; font-weight: 700; letter-spacing: 2.2px; text-transform: uppercase;
    color: var(--brand-blue);
  }
  .services-list {
    position: absolute; left: 34px; top: 106px; list-style: none;
    font-size: 12.6px; font-weight: 400; letter-spacing: 1.7px; line-height: 17.4px;
    text-transform: uppercase; color: var(--ink-body);
  }
  .services-list li::before { content: "-"; }
  .call-to-action {
    position: absolute; left: 37px; top: 302px;
    font-size: 14px; font-weight: 700; letter-spacing: 2.1px; text-transform: uppercase;
    color: var(--ink-dark);
  }

  .brand { position: absolute; left: 31px; top: 36px; display: flex; align-items: center; gap: 14px; }
  .brand-dot { width: 86px; height: 86px; border-radius: 50%; background: var(--mark-grey); }
  .brand-name {
    color: var(--brand-blue); font-weight: 700; font-size: 34px; line-height: 38px;
    letter-spacing: -0.5px; text-transform: uppercase;
  }

  .person { position: absolute; right: 28px; top: 200px; text-align: right; }
  .person-name {
    color: var(--brand-blue); font-size: 26px; font-weight: 700; line-height: 30px;
    text-transform: uppercase;
  }
  .person-role { font-size: 17px; font-weight: 400; text-transform: uppercase; line-height: 20px; }

  .contact {
    position: absolute; right: 28px; top: 270px; text-align: right; list-style: none;
    font-size: 14px; letter-spacing: 1.4px; line-height: 19px; text-transform: uppercase;
  }
  .contact b { font-weight: 700; }
</style>
</head>
<body>
<main class="canvas">
  <section class="card card--back">
    <div class="card-decoration" role="img" aria-label="Faint phoenix illustration"></div>
    <h1 class="services-title">Willow Ascent Services</h1>
    <ul class="services-list">
      <li>Rise from the ashes and live the life you want</li>
      <li>Personal and business success through</li>
      <li>Coaching | Hypnotherapy | Facilitation</li>
      <li>Greta Halloway MBA specializing in project management</li>
      <li>Founder</li>
      <li>Certified clinical hypnotherapist</li>
      <li>Certified neuro linguistic programming practitioner</li>
      <li>Certified life coach</li>
    </ul>
    <p class="call-to-action">Contact us now for your free 20min assessment</p>
  </section>

  <section class="card card--front">
    <div class="card-decoration" role="img" aria-label="Faint phoenix wing illustration"></div>
    <div class="brand">
      <span class="brand-dot"></span>
      <span class="brand-name">Willow<br>Ascent</span>
    </div>
    <div class="person">
      <p class="person-name">Tomas Wren</p>
      <p class="person-role">Direcotor</p>
    </div>
    <ul class="contact">
      <li><b>M.</b>0412 835 076</li>
      <li><b>E.</b> willowascent.au@kestrelmail.com</li>
      <li><b>W.</b> www.willowascent.com.au</li>
    </ul>
  </section>
</main>
</body>
</html>
```